Book Cover Design for Millennial

I need a book cover design for my book Harbor Ascent. The subtitle of the book is How to Own, Enjoy and Excel in Your Career.

I'm a career coach who helps millennial career professionals. I myself am a millennial but on the older end (34). I've dealt and been through most of the challenges millennials are facing as career professionals and I wrote this book with the thought of providing guidance and aid to getting past those challenges and shedding light on fundamental habits and practices that will help them excel in their careers. In addition, the book will help them prepare millennials for our turn as the leaders, managers, etc moving forward in corporate America. The final design should have the main title of the book in it as the focal point but not the subtitle. I want the cover to communicate something NEW, Bold, Youthful, non-traditional. I want it to stick out while still maintaining a sleek and Professional look.
Updates

Hello, Designers! I want to thank you all for your submissions! The work is amazing and I greatly appreciate it. If you would I want to help out in this process by adding a few updates based on the submissions I have seen. The concept I think that is coming close to hitting the mark is Tessel Works. What I would like to see changed about the concept is the following: Change the outfits to be more Millennial Career Professional. I have attached some ideas to the brief. I want to replace this picture with one of multiple millennials anywhere from 3 and up. I would like the pic to have diversity in it representing most races of people in the USA. I would like my name beneath harbor ascent. I'm not a known author yet so having my name that big my distract from the title of the book. Can we make the title a little bigger and so far I like the background.Thanks, DW Added Friday, September 30, 2016

Target Market(s)

Millennial Career Professionals (18 - 34 age group)

Industry/Entity Type

Life Coaching

Logo Text

Harbor Ascent

Requirements
Must have
• communicate something NEW, Bold, Youthful, non-traditional. I want it to stick out while still maintaining a sleek and Professional look.
Nice to have
• something that goes with my brand
• http://www.darnellwhitby-example.com
Should not have
• Nothing 3D or a logo that is hard to read when placed on stationeries, business cards etc

```html
<!DOCTYPE html>
<html lang="en">
<head>
<meta charset="utf-8">
<title>Harbor Ascent — Book Cover</title>
<link rel="stylesheet" href="https://fonts.googleapis.com/css2?family=Oswald:wght@500;600&family=Crimson+Pro:wght@400&display=swap">
<style>
  :root {
    --page-bg: #f3f4f6;
    --cover-bg: #ffffff;
    --ink: #0b0b0b;
    --accent-blue: #0c93c9;
    --photo-light: #eef2f5;
    --photo-mid: #c9d3dc;
    --photo-dark: #2c3445;
  }
  * { box-sizing: border-box; margin: 0; padding: 0; }
  html, body {
    width: 1200px;
    height: 1135px;
    overflow: hidden;
    background: var(--page-bg);
  }
  .canvas {
    position: relative;
    width: 1200px;
    height: 1135px;
  }
  .book-cover {
    position: absolute;
    left: 270px;
    top: 37px;
    width: 660px;
    height: 1060px;
    background: var(--cover-bg);
    overflow: hidden;
    box-shadow: 0 2px 10px rgba(0,0,0,0.12);
  }
  .cover-photo {
    display: block;
    width: 660px;
    height: 480px;
  }
  .cover-text {
    position: absolute;
    left: 50px;
    right: 50px;
    top: 515px;
  }
  .title {
    font-family: "Oswald", sans-serif;
    font-weight: 600;
    text-transform: uppercase;
    line-height: 0.98;
    letter-spacing: 2px;
  }
  .title-line {
    display: block;
    font-size: 156px;
  }
  .title-line--dark { color: var(--ink); }
  .title-line--blue { color: var(--accent-blue); }
  .subtitle {
    position: absolute;
    left: 0;
    right: 0;
    top: 862px;
    text-align: center;
    font-family: "Crimson Pro", serif;
    font-size: 29px;
    color: var(--ink);
  }
  .author-name {
    position: absolute;
    left: 0;
    right: 0;
    top: 955px;
    text-align: center;
    font-family: "Oswald", sans-serif;
    font-weight: 500;
    font-size: 36px;
    letter-spacing: 0.5px;
    color: var(--ink);
    text-transform: uppercase;
  }
</style>
</head>
<body>
  <div class="canvas">
    <article class="book-cover">
      <svg class="cover-photo" viewBox="0 0 660 480" role="img" aria-label="Photo of four smiling young professionals in business attire giving a thumbs up in a bright office">
        <defs>
          <linearGradient id="photoBackdrop" x1="0" y1="0" x2="0" y2="1">
            <stop offset="0" stop-color="var(--photo-light)"/>
            <stop offset="0.55" stop-color="var(--photo-mid)"/>
            <stop offset="1" stop-color="var(--photo-dark)"/>
          </linearGradient>
        </defs>
        <rect width="660" height="480" fill="url(#photoBackdrop)"/>
      </svg>

      <div class="cover-text">
        <h1 class="title">
          <span class="title-line title-line--dark">Harbor</span>
          <span class="title-line title-line--blue">Ascent</span>
        </h1>
      </div>

      <p class="subtitle">How to Own, Enjoy and Excel in Your Career</p>
      <p class="author-name">Author Name</p>
    </article>
  </div>
</body>
</html>
```